Tarsel Energy Letter Head- with all subsidiaries

We need a letterhead that will showcase all Tarsel Energy subsidiaries, while still have Tarsel Energy logo ontop.

```html
<!DOCTYPE html>
<html lang="en">
<head>
<meta charset="utf-8">
<title>Tarsel Energy Letterhead</title>
<link href="https://fonts.googleapis.com/css2?family=Open+Sans:wght@400;600&display=swap" rel="stylesheet">
<style>
  :root {
    --backdrop: #e4e4e4;
    --paper: #ffffff;
    --ink: #4a4a4a;
    --ink-dark: #2f2f2f;
    --gold: #c9a961;
    --charcoal: #3b3b3d;
  }
  html, body {
    margin: 0;
    padding: 0;
    width: 1040px;
    height: 1200px;
    overflow: hidden;
    background: var(--backdrop);
    font-family: "Open Sans", sans-serif;
    color: var(--ink);
  }
  .letterhead {
    position: absolute;
    left: 78px;
    top: 31px;
    width: 885px;
    height: 1138px;
    background: var(--paper);
    box-shadow: 0 2px 10px rgba(0,0,0,0.18);
    overflow: hidden;
  }
  .brand {
    position: absolute;
    left: 84px;
    top: 62px;
    display: flex;
    align-items: center;
    gap: 12px;
  }
  .brand-square {
    width: 54px;
    height: 54px;
    background: var(--gold);
  }
  .brand-name {
    font-size: 34px;
    font-weight: 600;
    color: var(--charcoal);
    letter-spacing: 0.5px;
  }
  .contact {
    position: absolute;
    right: 88px;
    top: 76px;
    text-align: right;
    font-size: 13.5px;
    line-height: 17.5px;
    color: var(--ink-dark);
  }
  .contact-line {
    display: flex;
    justify-content: flex-end;
    align-items: center;
    gap: 6px;
  }
  .contact-line svg { width: 11px; height: 11px; fill: var(--ink-dark); }
  .letter-body {
    position: absolute;
    left: 84px;
    top: 205px;
    width: 713px;
    font-size: 14px;
  }
  .letter-body p { margin: 0; }
  .issue-date { margin-bottom: 16px !important; }
  .recipient { line-height: 17px; margin-bottom: 48px !important; }
  .salutation { margin-bottom: 30px !important; }
  .paragraph {
    line-height: 25.8px;
    text-align: justify;
    hyphens: auto;
    -webkit-hyphens: auto;
    margin-bottom: 25px !important;
  }
  .closing { margin-top: 50px !important; margin-bottom: 56px !important; }
  .signatory-name { font-size: 18px; color: var(--ink-dark); margin-bottom: 4px !important; }
  .signatory-title { font-size: 14px; }
  .subsidiaries {
    position: absolute;
    left: 84px;
    top: 1016px;
    width: 713px;
    display: flex;
    justify-content: space-between;
    align-items: center;
  }
  .subsidiary {
    display: flex;
    align-items: center;
    gap: 4px;
    font-size: 10px;
    font-weight: 600;
    color: var(--charcoal);
    line-height: 12px;
    white-space: nowrap;
  }
  .subsidiary-square {
    flex: none;
    width: 10px;
    height: 10px;
    background: var(--gold);
  }
  .footer-wave {
    position: absolute;
    left: 0;
    bottom: 0;
    width: 885px;
    height: 70px;
  }
</style>
</head>
<body>
  <main class="letterhead">
    <header>
      <div class="brand">
        <span class="brand-square"></span>
        <span class="brand-name">Tarsel Energy</span>
      </div>
      <div class="contact">
        <div class="contact-line">044-555 010 482
          <svg viewBox="0 0 12 12"><path d="M1 5c0-2 2-3 5-3s5 1 5 3l-2 1-1-2H4L3 6 1 5zM3 7h6l1 4H2z"/></svg>
        </div>
        <div class="contact-line">info@tarselenergy.com
          <svg viewBox="0 0 12 12"><path d="M1 2h10v8H1zM2 3v1l4 3 4-3V3L6 6z"/></svg>
        </div>
        <div class="contact-line">www.tarselenergy.com
          <svg viewBox="0 0 12 12"><circle cx="6" cy="6" r="5.5"/></svg>
        </div>
      </div>
    </header>

    <section class="letter-body">
      <p class="issue-date">Issuing Date: May 5, 2018</p>
      <p class="recipient">Name Of Employee Mr. XYZABC<br>Address of Employee<br>Address Line 2 etc..</p>
      <p class="salutation">Dear Mr.XYZABC</p>
      <p class="paragraph">Lorem Ipsum has been the industry's standard dummy text ever since the 1500s, when an unknown printer took a galley of type and scrambled it to make a type specimen book. It has survived not only five centuries, but also the leap into electronic typesetting, remaining essentially unchanged. It was popularised in the 1960s with the release of Quillmark sheets containing Lorem Ipsum passages, and more recently with desktop publishing software like Folio PageCraft including versions of Lorem Ipsum.</p>
      <p class="paragraph">Lorem Ipsum is simply dummy text of the printing and typesetting industry. Lorem Ipsum has been the industry's standard dummy text ever since the 1500s, when an unknown printer took a galley of type and scrambled it to make a type specimen book.</p>
      <p class="paragraph">It has survived not only five centuries, but also the leap into electronic typesetting, remaining essentially unchanged. It was popularised in the 1960s with the release of Quillmark sheets containing Lorem IpsumIpsum passages.</p>
      <p class="closing">Yours Sincerely</p>
      <p class="signatory-name">Daniel Hartley</p>
      <p class="signatory-title">Managing Director</p>
    </section>

    <footer>
      <div class="subsidiaries">
        <div class="subsidiary"><span class="subsidiary-square"></span>Volt Line Electric</div>
        <div class="subsidiary"><span class="subsidiary-square"></span>Brightwire Electrical</div>
        <div class="subsidiary"><span class="subsidiary-square"></span>Tarsel Logistics</div>
        <div class="subsidiary"><span class="subsidiary-square"></span>Tarsel Caribbean</div>
        <div class="subsidiary"><span class="subsidiary-square"></span>Tarsel Aviation</div>
        <div class="subsidiary"><span class="subsidiary-square"></span>Tarsel Acquisitions</div>
      </div>
      <svg class="footer-wave" viewBox="0 0 885 70" preserveAspectRatio="none">
        <path d="M0 2 Q442 70 885 2 L885 70 L0 70 Z" fill="var(--gold)"/>
        <path d="M0 18 Q442 82 885 18 L885 70 L0 70 Z" fill="var(--charcoal)"/>
      </svg>
    </footer>
  </main>
</body>
</html>
```